Law Firm Business Cards/Letterhead/Envelopes
Holloway Law Firm, PLLC Business Cards/Letterhead/Envelopes
I need double sided standard sized Business Card [3.5" x 2"]
Selective use of Same font as logo and also may use other type of font
Simple
Martin J. Holloway
Attorney & Counselor at Law
2650 Prairie Ridge Road - Suite 1200
Bloomington, MN 55429
martin@holfirm.example
www.holfirm.example
The front of the card I would like to incorporate my logo and firm name, my name, title, address, numbers/fax, email and website. The business card WILL NOT have curved corners. Open to different possibilities but dont want the card too busy....I'd prefer something on the "simple" side...Same goes for envelope and letterhead.
Probably just Logo, Firm name and address all in upper left of envelope.
Letterhead - Logo and firm name up top somewhere...address at bottom....do not include my name and my title on letterhead.
The back of the card I would like to only incorporate the Logo and website OR Logo and firm name and website. The business card WILL NOT have curved corners. Possibly a different color back (possibly grey), but not necessarily. Possibly a watermark of the logo used somewhere...open to different possibilities but dont want the card too busy....I'd prefer something on the "simple" side...
Logo to the Left
Folder Template

```html
<!DOCTYPE html>
<html lang="en">
<head>
<meta charset="utf-8">
<title>Holloway Law Firm, PLLC – Business Card</title>
<link rel="stylesheet" href="https://fonts.googleapis.com/css2?family=Tinos:ital,wght@0,400;0,700;1,700&display=swap">
<style>
  :root {
    --backdrop: #e8e5e0;
    --card-white: #ffffff;
    --navy-deep: #0e2748;
    --navy-mid: #234e80;
    --navy-light: #3a6ca5;
    --ink-navy: #1d3f6b;
    --swoosh-grey: #a9adb3;
    --swoosh-light: #dfe1e4;
    --text-light: #ffffff;
  }
  * { margin: 0; padding: 0; box-sizing: border-box; }
  html, body {
    width: 1200px; height: 965px; overflow: hidden;
    background: var(--backdrop);
  }
  .canvas {
    position: relative; width: 1200px; height: 965px;
    display: flex; align-items: center; justify-content: center;
  }
  .business-card {
    position: relative; width: 1000px; height: 571px;
    background: var(--card-white);
    overflow: hidden;
    box-shadow: 0 6px 18px rgba(0,0,0,0.18);
    font-family: "Tinos", "Times New Roman", serif;
  }
  .card-art { position: absolute; inset: 0; width: 100%; height: 100%; }
  .contact-panel {
    position: absolute; left: 34px; top: 0; width: 480px; height: 100%;
    color: var(--text-light);
  }
  .person-name { position: absolute; top: 48px; font-size: 32px; font-weight: 700; }
  .person-title { position: absolute; top: 90px; left: 18px; font-size: 23px; font-weight: 700; font-style: italic; }
  .office-address { position: absolute; top: 270px; font-size: 25px; font-style: normal; line-height: 1.22; }
  .contact-list { position: absolute; top: 362px; list-style: none; font-size: 24px; }
  .contact-list li { display: flex; align-items: center; height: 32px; }
  .contact-list svg { width: 22px; height: 22px; margin-right: 14px; fill: var(--text-light); flex: none; }
  .contact-list .at-sign { width: 22px; margin-right: 14px; font-weight: 700; text-align: center; }
  .firm-identity {
    position: absolute; left: 600px; top: 78px; width: 400px;
    display: flex; flex-direction: column; align-items: center;
    color: var(--ink-navy); font-weight: 400;
  }
  .firm-mark { width: 74px; height: 74px; background: var(--ink-navy); margin-bottom: 16px; }
  .firm-name { font-size: 64px; line-height: 1; letter-spacing: 1px; }
  .firm-suffix { font-size: 32px; letter-spacing: 3px; margin-top: 6px; }
</style>
</head>
<body>
<main class="canvas">
  <article class="business-card">
    <svg class="card-art" viewBox="0 0 1000 571" preserveAspectRatio="none" aria-hidden="true">
      <defs>
        <radialGradient id="panelBlue" cx="0.4" cy="0.55" r="0.7">
          <stop offset="0" stop-color="#3a6ca5"/>
          <stop offset="0.55" stop-color="#234e80"/>
          <stop offset="1" stop-color="#0e2748"/>
        </radialGradient>
        <linearGradient id="swooshGrey" x1="0" y1="0" x2="0" y2="1">
          <stop offset="0" stop-color="#dfe1e4"/>
          <stop offset="0.45" stop-color="#a9adb3"/>
          <stop offset="1" stop-color="#dfe1e4"/>
        </linearGradient>
      </defs>
      <path d="M0,0 H478 C568,110 615,250 560,385 C522,475 468,535 432,571 H0 Z" fill="url(#swooshGrey)" transform="translate(14,0)"/>
      <path d="M0,0 H478 C568,110 615,250 560,385 C522,475 468,535 432,571 H0 Z" fill="url(#panelBlue)"/>
    </svg>

    <section class="contact-panel">
      <h1 class="person-name">Martin J. Holloway</h1>
      <p class="person-title">Attorney &amp; Counselor at Law</p>
      <address class="office-address">2650 Prairie Ridge Road - Suite 1200<br>Bloomington, MN 55429</address>
      <ul class="contact-list">
        <li><svg viewBox="0 0 24 24"><path d="M6.6 10.8c1.4 2.8 3.8 5.1 6.6 6.6l2.2-2.2c.3-.3.7-.4 1-.2 1.1.4 2.3.6 3.6.6.6 0 1 .4 1 1V20c0 .6-.4 1-1 1C10.6 21 3 13.4 3 4c0-.6.4-1 1-1h3.5c.6 0 1 .4 1 1 0 1.3.2 2.5.6 3.6.1.3 0 .7-.2 1z"/></svg>(1) (800) 555-0142</li>
        <li><svg viewBox="0 0 24 24"><path d="M6.6 10.8c1.4 2.8 3.8 5.1 6.6 6.6l2.2-2.2c.3-.3.7-.4 1-.2 1.1.4 2.3.6 3.6.6.6 0 1 .4 1 1V20c0 .6-.4 1-1 1C10.6 21 3 13.4 3 4c0-.6.4-1 1-1h3.5c.6 0 1 .4 1 1 0 1.3.2 2.5.6 3.6.1.3 0 .7-.2 1z"/></svg>(952) 555-0189</li>
        <li><svg viewBox="0 0 24 24"><path d="M6 3h10v5H6zM3 9h18v9h-3v3H6v-3H3zm5 6v4h8v-4z"/></svg>(952) 555-0188</li>
        <li><span class="at-sign">@</span>martin@holfirm.example</li>
        <li><svg viewBox="0 0 24 24"><path d="M12 2a10 10 0 1 0 0 20 10 10 0 0 0 0-20zm0 2c.9 0 2.2 1.7 2.8 5H9.2C9.8 5.7 11.1 4 12 4zM4.3 11h2.8a18 18 0 0 0 0 2H4.3a8 8 0 0 1 0-2zm4.8 0h5.8a16 16 0 0 1 0 2H9.1a16 16 0 0 1 0-2zm7.8 0h2.8a8 8 0 0 1 0 2h-2.8a18 18 0 0 0 0-2zM9.2 15h5.6c-.6 3.3-1.9 5-2.8 5s-2.2-1.7-2.8-5z"/></svg>www.holfirm.example</li>
      </ul>
    </section>

    <section class="firm-identity">
      <div class="firm-mark"></div>
      <p class="firm-name">HOLLOWAY</p>
      <p class="firm-suffix">LAW FIRM, PLLC</p>
    </section>
  </article>
</main>
</body>
</html>
```